Business Card Design needed for logo design project

This project is linked to a href='http://jobs.pixelfennel.example/job.aspx?id=412907'Tide Nook: Design a logo for our new trailer boat syndication business in Sydney
Our company needs a Business Card Design. Please refer to our original project in the link above.
I would like a relatively simple and classy business card design. could you please also use small symbols for identifying contact info eg. mobile, web and email?
Updates
Please see my new project to design a business card for a trailer boat syndication business in Sydney, Australia.
Industry/Entity Type
Business
Look and feel
Each slider illustrates characteristics of the customer's brand and the style your logo design should communicate.

```html
<!DOCTYPE html>
<html lang="en">
<head>
<meta charset="utf-8">
<title>Tide Nook – Business Card</title>
<link rel="stylesheet" href="https://fonts.googleapis.com/css2?family=Source+Sans+3:wght@400;600;700&display=swap">
<style>
  :root {
    --teal: #2bafba;
    --ink: #1b1b1b;
    --text: #1f1f1f;
    --paper: #ffffff;
    --stage: #3d3d3d;
    --rule: #3a3a3a;
  }
  * { margin: 0; padding: 0; box-sizing: border-box; }
  html, body {
    width: 1200px; height: 750px; overflow: hidden;
    background: var(--stage);
    font-family: "Source Sans 3", "Myriad Pro", Arial, sans-serif;
  }
  .canvas { position: relative; width: 1200px; height: 750px; }
  .card {
    position: absolute; top: 210px;
    width: 545px; height: 313px;
    border-radius: 24px; overflow: hidden;
    transform: scale(0.9375); transform-origin: 0 0;
  }
  .card--front { left: 78px; background: var(--teal); }
  .card--back { left: 609px; background: var(--paper); }

  .front-name {
    position: absolute; left: 0; right: 0; top: 160px;
    text-align: center; color: var(--paper);
    font-weight: 700; font-size: 46px; letter-spacing: 0.5px;
  }

  .back-shapes { position: absolute; inset: 0; }
  .person-name {
    position: absolute; left: 31px; top: 48px;
    color: var(--teal); font-weight: 700; font-size: 21px;
  }
  .person-title {
    position: absolute; left: 33px; top: 73px;
    color: var(--text); font-size: 15px;
  }
  .contact-list { position: absolute; left: 31px; top: 120px; list-style: none; }
  .contact-item {
    display: flex; align-items: center; gap: 8px;
    height: 21.3px; font-size: 15.5px; color: var(--text);
  }
  .contact-icon {
    width: 15px; height: 15px; border-radius: 2px;
    background: var(--teal); display: flex; align-items: center; justify-content: center;
    color: var(--paper); font-size: 9px; font-weight: 700;
  }
  .contact-icon svg { width: 11px; height: 11px; }
  .address {
    position: absolute; left: 31px; top: 245px;
    display: flex; gap: 8px; color: var(--paper); font-size: 15.5px; line-height: 20px;
  }
  .address-icon {
    width: 15px; height: 15px; margin-top: 2px; border-radius: 2px;
    background: var(--paper); display: flex; align-items: center; justify-content: center;
  }
  .back-name {
    position: absolute; left: 276px; top: 150px; width: 225px;
    text-align: center; color: var(--teal);
    font-weight: 700; font-size: 34px;
  }
</style>
</head>
<body>
<main class="canvas">
  <section class="card card--front" aria-label="Card front">
    <div class="front-name">Tide Nook</div>
  </section>

  <section class="card card--back" aria-label="Card back">
    <svg class="back-shapes" viewBox="0 0 545 313" width="545" height="313" aria-hidden="true">
      <polygon points="10,0 246,0 236,16 10,16" fill="var(--teal)"/>
      <polygon points="250,0 545,0 545,16 240,16" fill="var(--ink)"/>
      <line x1="95" y1="86" x2="537" y2="86" stroke="var(--rule)" stroke-width="1"/>
      <polygon points="0,239 275,239 250,289 0,289" fill="var(--ink)"/>
      <polygon points="311,208 545,208 545,289 242,289" fill="var(--teal)"/>
    </svg>

    <div class="person-name">Your Name</div>
    <div class="person-title">Your title</div>

    <ul class="contact-list">
      <li class="contact-item"><span class="contact-icon"><svg viewBox="0 0 12 12"><path d="M3 1l2 2.5-1 1.2a6 6 0 0 0 3.3 3.3l1.2-1L11 9l-1.2 1.8C5.5 10.5 1.5 6.5 1.2 2.2z" fill="#fff"/></svg></span>0123 456 789</li>
      <li class="contact-item"><span class="contact-icon"><svg viewBox="0 0 12 12"><rect x="3" y="1" width="6" height="10" rx="1" fill="none" stroke="#fff" stroke-width="1.3"/></svg></span>0123 456 789</li>
      <li class="contact-item"><span class="contact-icon">Fx</span>0123 456 789</li>
      <li class="contact-item"><span class="contact-icon">@</span>youremail@mail.com</li>
      <li class="contact-item"><span class="contact-icon"><svg viewBox="0 0 12 12"><circle cx="6" cy="6" r="4.6" fill="none" stroke="#fff" stroke-width="1"/><ellipse cx="6" cy="6" rx="2" ry="4.6" fill="none" stroke="#fff" stroke-width="1"/><line x1="1.4" y1="6" x2="10.6" y2="6" stroke="#fff" stroke-width="1"/></svg></span>www.yourwebdite.com</li>
    </ul>

    <div class="address">
      <span class="address-icon"><svg viewBox="0 0 12 12" width="11" height="11"><path d="M6 1a3.3 3.3 0 0 1 3.3 3.3C9.3 7 6 11 6 11S2.7 7 2.7 4.3A3.3 3.3 0 0 1 6 1z" fill="var(--ink)"/><circle cx="6" cy="4.3" r="1.2" fill="#fff"/></svg></span>
      <span>our address put here<br>your address put here</span>
    </div>

    <div class="back-name">Tide Nook</div>
  </section>
</main>
</body>
</html>
```